Industrial Automation company requires a business card design

Valtrin Automation provides design & build of Automated Equipment for manufacturing industry.
www.valtrinautomation.example
The equipment we design is used for manufacturing in sectors such as medical device, pharmaceutical, aerospace and electronics.
We require a new business card design which incorporates our (New) logo and the key message words:
Automated Equipment:
Design, Build, Control, Test, Support

```html
<!DOCTYPE html>
<html lang="en">
<head>
<meta charset="utf-8">
<title>Valtrin Automation – Business Card</title>
<link rel="stylesheet" href="https://fonts.googleapis.com/css2?family=Exo+2:wght@400;500;600;700&display=swap">
<style>
  :root {
    --brand-green: #0e7a3e;
    --ink-grey: #555555;
    --card-white: #ffffff;
    --backdrop: #3b3b3b;
    --on-green: #ffffff;
  }
  * { margin: 0; padding: 0; box-sizing: border-box; }
  html, body { width: 1105px; height: 1200px; overflow: hidden; }
  body {
    background: var(--backdrop);
    font-family: "Exo 2", sans-serif;
    position: relative;
  }
  .card {
    position: absolute;
    left: 193px;
    width: 721px;
    height: 410px;
  }
  .card--front { top: 167px; background: var(--card-white); }
  .card--back { top: 623px; background: var(--brand-green); }

  .brand {
    position: absolute;
    display: flex;
    align-items: center;
    gap: 12px;
    font-weight: 700;
    letter-spacing: 1px;
    text-transform: uppercase;
    white-space: nowrap;
  }
  .brand__mark { width: 22px; height: 22px; background: currentColor; flex: none; }
  .card--front .brand { left: 46px; top: 58px; font-size: 30px; color: var(--brand-green); }

  .person { position: absolute; right: 46px; top: 174px; text-align: right; }
  .person__name { font-size: 25px; font-weight: 600; color: var(--brand-green); letter-spacing: .5px; }
  .person__role { font-size: 18px; color: var(--ink-grey); margin-top: 2px; }

  .address { position: absolute; left: 46px; top: 198px; font-size: 18px; line-height: 26px; color: var(--ink-grey); }
  .contacts { position: absolute; left: 46px; top: 258px; list-style: none; font-size: 18px; color: var(--ink-grey); }
  .contacts li { display: flex; align-items: center; gap: 10px; height: 28px; }
  .contacts svg { width: 16px; height: 16px; fill: var(--brand-green); flex: none; }

  .back-block {
    position: absolute;
    right: 34px;
    top: 248px;
    width: 380px;
    text-align: center;
    color: var(--on-green);
  }
  .back-block .brand { position: static; justify-content: center; font-size: 34px; }
  .offer { font-size: 21px; font-weight: 600; margin-top: 12px; }
  .services { font-size: 17px; margin-top: 6px; word-spacing: 1px; }
  .services span::after { content: "•"; margin: 0 4px; }
  .services span:last-child::after { content: ""; margin: 0; }
</style>
</head>
<body>
  <section class="card card--front" aria-label="Business card front">
    <div class="brand"><span class="brand__mark"></span>Valtrin Automation</div>

    <div class="person">
      <p class="person__name">MARCUS HALE</p>
      <p class="person__role">CEO/Founder</p>
    </div>

    <address class="address" style="font-style:normal">
      2140 Larch Street<br>
      Fairbanks, Alaska 34610
    </address>

    <ul class="contacts">
      <li>
        <svg viewBox="0 0 16 16" aria-hidden="true"><path d="M3.5 1.5l2.3 0 1.2 3.2-1.6 1.2c.8 1.8 2.2 3.2 4 4l1.2-1.6 3.2 1.2 0 2.3c0 .9-.8 1.7-1.7 1.7C6.6 13.5 2.5 9.4 1.8 3.2c0-.9.8-1.7 1.7-1.7z"/></svg>
        555 210 4837
      </li>
      <li>
        <svg viewBox="0 0 16 16" aria-hidden="true"><path d="M4 1h8v4H4zM1 6h14v6h-3v3H4v-3H1zM5 10v4h6v-4z"/></svg>
        555 318 6092
      </li>
      <li>
        <svg viewBox="0 0 16 16" aria-hidden="true"><path d="M1 3h14v1.2L8 9 1 4.2zM1 5.8l7 4.8 7-4.8V13H1z"/></svg>
        info@valtrinautomation.example
      </li>
      <li>
        <svg viewBox="0 0 16 16" aria-hidden="true"><circle cx="8" cy="8" r="7"/><path d="M2 8h12M8 1c2 2 2 12 0 14M8 1c-2 2-2 12 0 14" stroke="#fff" stroke-width="1" fill="none"/></svg>
        www.valtrinautomation.example
      </li>
    </ul>
  </section>

  <section class="card card--back" aria-label="Business card back">
    <div class="back-block">
      <div class="brand"><span class="brand__mark"></span>Valtrin Automation</div>
      <p class="offer">Automated Equipment</p>
      <p class="services"><span>Design</span><span>Build</span><span>Control</span><span>Test</span><span>Support</span></p>
    </div>
  </section>
</body>
</html>
```